Poster for Office

Looking for an edgy, beautiful poster to hang up in my office that uses the quotes located below and potentially the image attached.

Title: Hadley's Maxims

Must have the following quotes included (punctuation and capitalization are flexible, do what you think looks the best they also don't need the quotation symbols):

"Don't order fish at a steakhouse"
"Be bold. The more you tell, the more you sell"
"admit nothing, deny everything, launch counterattack."
"avoid obviousness"
"never do anything until you're ready to do it"
"look good=feel good"
"always keep the advantage"
"never complain, never explain"
"Lay low, play dumb, keep moving"

Quotes

• Title: Hadley's Maxims

"avoid obviousness"
"look good=feel good"

```html
<!DOCTYPE html>
<html lang="en">
<head>
<meta charset="UTF-8">
<title>Hadley's Maxims – Office Poster</title>
<link href="https://fonts.googleapis.com/css2?family=Archivo+Black&display=swap" rel="stylesheet">
<style>
  :root {
    --backdrop: #b8a58c;
    --stone-light: #b9b9b7;
    --stone-mid: #9d9d9b;
    --stone-dark: #7e7e7c;
    --ink: #232323;
    --ink-highlight: rgba(255, 255, 255, 0.28);
  }
  * { margin: 0; padding: 0; box-sizing: border-box; }
  html, body {
    width: 1200px;
    height: 1000px;
    overflow: hidden;
    background: var(--backdrop);
  }
  .canvas {
    width: 1200px;
    height: 1000px;
    display: flex;
    align-items: center;
    justify-content: center;
  }
  .poster {
    width: 640px;
    height: 920px;
    padding: 96px 56px 60px;
    background:
      radial-gradient(circle at 25% 20%, var(--stone-light) 0%, transparent 55%),
      radial-gradient(circle at 80% 75%, var(--stone-dark) 0%, transparent 60%),
      linear-gradient(160deg, var(--stone-light), var(--stone-mid) 55%, var(--stone-dark));
    font-family: "Archivo Black", "Arial Black", sans-serif;
    color: var(--ink);
    text-transform: uppercase;
    text-shadow: 0 1px 0 var(--ink-highlight);
    display: flex;
    flex-direction: column;
  }
  .poster-title {
    font-size: 46px;
    font-weight: 400;
    text-align: center;
    letter-spacing: 0.5px;
    margin-bottom: 26px;
  }
  .maxims { list-style: none; }
  .maxim-line {
    line-height: 1.02;
    white-space: nowrap;
    letter-spacing: -0.3px;
  }
  .size-xs { font-size: 14px; }
  .size-s  { font-size: 20px; }
  .size-m  { font-size: 23px; }
  .size-l  { font-size: 32px; }
  .size-xl { font-size: 41px; }
  .size-xxl { font-size: 62px; line-height: 1; }
</style>
</head>
<body>
<main class="canvas">
  <article class="poster">
    <h1 class="poster-title">Hadley's Maxims</h1>
    <ul class="maxims">
      <li class="maxim-line"><span class="size-m">1. Don't order fish</span> <span class="size-xs">at a steakhouse</span></li>
      <li class="maxim-line size-m">2. Be bold the more you tell</li>
      <li class="maxim-line size-xl">The more you sell</li>
      <li class="maxim-line"><span class="size-m">3. Admit</span> <span class="size-xs">nothing,</span> <span class="size-m">deny</span> <span class="size-xs">everything</span></li>
      <li class="maxim-line size-l">Launch counterattack</li>
      <li class="maxim-line"><span class="size-m">4. Avoid</span> <span class="size-xl">obviousness</span></li>
      <li class="maxim-line size-m">5. Never do anything until</li>
      <li class="maxim-line"><span class="size-xl">You're ready</span> <span class="size-m">to do it</span></li>
      <li class="maxim-line size-m">6. Look good = feel good</li>
      <li class="maxim-line size-s">7. Always keep the advantage</li>
      <li class="maxim-line"><span class="size-s">8. Never</span> <span class="size-xs">complain</span> <span class="size-s">never</span> <span class="size-xs">explain</span></li>
      <li class="maxim-line"><span class="size-l">9. Lay low</span> <span class="size-m">play dumb</span></li>
      <li class="maxim-line size-xxl">Keep moving</li>
    </ul>
  </article>
</main>
</body>
</html>
```